Rivet Ridge Works Client Handout

We need a cover sheet for our processes flyer that we will be handing out to our clients. Attached is a set of stairs that our company has erected, as well as our logos and a rough draft of what we are looking for. We would like the stairs in our image to be sharpened if at all possible, taken out from the background, and instead placed atop an image of a beautiful Arizona sunset/landscape. We would like the text to be editable and we would like to retain the rights to the product, as our language on this project is still being revised. We would also like the placement/positioning of our logos to be refined to look more modernized and professional.

Target Market(s)

Construction contractors, vendors and prospective builders.

Industry/Entity Type

Structural Steel

Requirements
Must have
• • clean up the background
• see if the stair image could be sharpened at all
• Put a beautiful AZ sunset behind it
• Refine location/layout of the RRW logo & header up top to make it a modernized, professional handout that we can give to clients
• NOTE: we may have a small amount of refining of the language used on the sub bullets so want to make sure we have the rights to the document to edit and revise it
Nice to have
• Please use our logo on this.
We would like a very Arizona-esque looking background. See link below for examples

https://www.findlyquest.example/search?q=arizona+sunset&tbm=isch

```html
<!DOCTYPE html>
<html lang="en">
<head>
<meta charset="utf-8">
<title>Iron-Strong – Stairway to Success | Rivet Ridge Works</title>
<link href="https://fonts.googleapis.com/css2?family=Barlow+Semi+Condensed:wght@500;600&family=Saira+Stencil+One&family=Playfair+Display:wght@900&display=swap" rel="stylesheet">
<style>
  :root {
    --sky-top: #f4866a;
    --sky-mid: #f8ab72;
    --sky-low: #fcd889;
    --band-red: #d6202a;
    --tab-red: #b51f24;
    --card-yellow: #fdc52c;
    --ink: #231f20;
    --arrow-red: #d42027;
    --white: #ffffff;
    --desert-dusk: #6b83b4;
    --desert-glow: #f0853a;
    --desert-floor: #7a4a2c;
    --steel: #3a3430;
  }
  * { box-sizing: border-box; margin: 0; padding: 0; }
  html, body { width: 928px; height: 1200px; overflow: hidden; }
  body { font-family: "Barlow Semi Condensed", "Arial Narrow", sans-serif; color: var(--ink); }

  .handout {
    position: relative;
    width: 928px;
    height: 1200px;
    overflow: hidden;
    background: linear-gradient(180deg, var(--sky-top) 0%, var(--sky-mid) 25%, var(--sky-low) 55%, var(--sky-low) 100%);
  }
  .scenery { position: absolute; inset: 0; width: 928px; height: 1200px; }

  /* Header */
  .headline {
    position: absolute;
    left: 178px; top: 38px;
    width: 572px; height: 68px;
    display: flex; gap: 3px;
  }
  .headline span {
    flex: 1;
    background: #0d0d0d;
    color: var(--sky-top);
    font-family: "Saira Stencil One", "Stencil", sans-serif;
    font-size: 62px;
    line-height: 68px;
    text-align: center;
  }
  .headline span.dash { flex: 0.55; }
  .subhead {
    position: absolute;
    left: 0; right: 0; top: 116px;
    text-align: center;
    font-family: "Playfair Display", Georgia, serif;
    font-weight: 900;
    font-size: 38px;
    letter-spacing: 0.5px;
    color: #111;
  }

  /* Process steps */
  .step { position: absolute; }
  .step-tab {
    display: inline-block;
    background: var(--tab-red);
    color: var(--white);
    font-weight: 600;
    font-size: 23px;
    line-height: 37px;
    padding: 0 14px;
    border-radius: 6px 6px 0 0;
    margin-left: 14px;
  }
  .step-card {
    background: var(--card-yellow);
    border-radius: 8px;
    padding: 11px 14px 12px 14px;
    list-style: none;
  }
  .step-card li {
    position: relative;
    padding-left: 19px;
    font-size: 17.5px;
    font-weight: 500;
    line-height: 27px;
  }
  .step-card li::before {
    content: "";
    position: absolute;
    left: 0; top: 8px;
    width: 9px; height: 11px;
    background: var(--arrow-red);
    clip-path: polygon(0 0, 45% 0, 100% 50%, 45% 100%, 0 100%, 55% 50%);
  }
  .step-card li.cont::before { display: none; }

  .step-evaluate      { left: 48px;  top: 232px; width: 232px; }
  .step-deliver       { left: 557px; top: 380px; width: 232px; }
  .step-implement     { left: 48px;  top: 447px; width: 321px; }
  .step-strategize    { left: 559px; top: 580px; width: 320px; }
  .step-collaborate   { left: 48px;  top: 750px; width: 310px; }
  .step-discover      { left: 561px; top: 848px; width: 342px; }
  .step-relationships { left: 54px;  top: 927px; width: 309px; }

  /* Brand plate */
  .brand {
    position: absolute;
    left: 272px; top: 1005px;
    width: 356px; height: 195px;
    text-align: center;
  }
  .brand-mark {
    position: absolute;
    left: 158px; top: 60px;
    width: 40px; height: 40px;
    background: #6d6e71;
  }
  .brand-name {
    position: absolute;
    left: 0; right: 0; top: 118px;
    font-weight: 600;
    font-size: 23px;
    color: var(--ink);
  }
  .brand-tagline {
    position: absolute;
    left: 0; right: 0; top: 154px;
    font-weight: 500;
    font-size: 16px;
    color: var(--ink);
  }
</style>
</head>
<body>
<main class="handout">
  <svg class="scenery" viewBox="0 0 928 1200" aria-hidden="false">
    <defs>
      <linearGradient id="desertGrad" x1="0" y1="0" x2="0" y2="1">
        <stop offset="0" stop-color="var(--desert-dusk)"/>
        <stop offset="0.35" stop-color="#c9775c"/>
        <stop offset="0.55" stop-color="var(--desert-glow)"/>
        <stop offset="0.72" stop-color="#9a5a34"/>
        <stop offset="1" stop-color="var(--desert-floor)"/>
      </linearGradient>
      <linearGradient id="stairGrad" x1="0" y1="0" x2="0" y2="1">
        <stop offset="0" stop-color="var(--steel)" stop-opacity="0.85"/>
        <stop offset="1" stop-color="var(--steel)" stop-opacity="0.7"/>
      </linearGradient>
    </defs>
    <polygon points="0,186 928,660 928,678 0,268" fill="var(--band-red)"/>
    <polygon points="0,268 928,678 928,1200 0,1200" fill="url(#desertGrad)" role="img" aria-label="Arizona desert sunset with saguaro and cholla cacti and distant mountains"/>
    <rect x="272" y="212" width="348" height="864" rx="6" fill="url(#stairGrad)" role="img" aria-label="Steel switchback stair tower with railings erected by the company"/>
    <polygon points="450,1005 628,1200 272,1200" fill="var(--band-red)"/>
    <polygon points="450,1020 614,1200 286,1200" fill="var(--white)"/>
  </svg>

  <h1 class="headline" aria-label="Iron-Strong">
    <span>I</span><span>R</span><span>O</span><span>N</span><span class="dash">-</span><span>S</span><span>T</span><span>R</span><span>O</span><span>N</span><span>G</span>
  </h1>
  <p class="subhead">STAIRWAY TO SUCCESS</p>

  <section class="step step-evaluate">
    <h2 class="step-tab">Evaluate</h2>
    <ul class="step-card">
      <li>Post Project Assessment</li>
      <li>Net Promoter Score</li>
    </ul>
  </section>

  <section class="step step-deliver">
    <h2 class="step-tab">Deliver</h2>
    <ul class="step-card">
      <li>Safely erect steel</li>
      <li>Blink and We Are Done</li>
    </ul>
  </section>

  <section class="step step-implement">
    <h2 class="step-tab">Implement</h2>
    <ul class="step-card">
      <li>Contact During Fabrication</li>
      <li>(75% Completed Before We Shop Up)</li>
      <li class="cont">3D Models Provided</li>
    </ul>
  </section>

  <section class="step step-strategize">
    <h2 class="step-tab">Strategize</h2>
    <ul class="step-card">
      <li>Iron-Strong Expectations Meeting</li>
      <li>Smarter, Faster, Better (Coordinate to Maximize Prefabrication)</li>
    </ul>
  </section>

  <section class="step step-collaborate">
    <h2 class="step-tab">Collaborate</h2>
    <ul class="step-card">
      <li>Pre-Construction Value Engineering</li>
      <li>Budgeting Assistance</li>
    </ul>
  </section>

  <section class="step step-discover">
    <h2 class="step-tab">Discover</h2>
    <ul class="step-card">
      <li>Share our Steel Expertise (Best Practices)</li>
      <li>Identify Best Value Opportunities (What’s Best for the Project)</li>
    </ul>
  </section>

  <section class="step step-relationships">
    <h2 class="step-tab">Iron Strong Relationships</h2>
    <ul class="step-card">
      <li>Prior Success Foundation</li>
      <li>Zippered Relationships</li>
    </ul>
  </section>

  <footer class="brand">
    <div class="brand-mark"></div>
    <p class="brand-name">Rivet Ridge Works</p>
    <p class="brand-tagline">Your Solution Partner</p>
  </footer>
</main>
</body>
</html>
```